Childrens Business Card Design Project

We have an existing logo attached which we'd like to use as part of our new business card design.

The design needs to be relatively gender neutral and contain bright colours.

In terms of look and feel think:

Fun, Modern, Quality (as opposed to cheap!) and of course Party!

Single or double sided - i am not decided on either one yet - ideally i'd like to see designs for both because if you think stylistically it would benefit having two sides then please try it out!

I think the challenge here is finding a really good background colour (if you think it needs one) and also choosing an eye grabbing text that compliments the existing logo - do that an you are onto a winner! I have another image for the business (which i have attached) which uses stripes so i am keen to see a design that incorporates this to tie in all my collateral.

The copy required is as follows (not necesarily in this order)

Bookings/Enquiries:

Tilda

T: 0498 217 503
E: enquiries@brightfoxparties.example.au

ABN: 47 302 658 114

Any feedback on text is welcomed - please message me or add to the discussion.

Reason: Hi All, I have received some promising designs, but overall i am not impressed with the quality of the work so have extended the deadline as this project has been committed. I will aim to attach some business card examples to the brief tomorrow to give further guidance as a whole but please do not submit any designs on a generic background that are not related to the theme, have been carelessly placed with overlapping elements - it just looks sloppy. For those who have read the brief an incorporated stripes or even spots this is on target as it convey's a party theme, however please work on getting the colours for the contact details by either a bold solid strip to highlight or some other way to frame it. When it comes to the logo, some people have removed the characters all together and changed the colour of the wording - this is fine. Also feel free to balloons starts - but keep it classy and watch your placement of these. I hope this helps and for the designs i would like to see revisions for i will aim to get back to you individually over the next day or so. Many thanks all.

Target Market(s)

Mothers in the suburbs of Australia with a disposal able income, children aged between 1-7 years old.

Industry/Entity Type

Business

Requirements
Must have
• The font and wording positioning must compliment the logo.

```html
<!DOCTYPE html>
<html lang="en">
<head>
<meta charset="utf-8">
<title>Bright Fox – Business Card</title>
<link rel="stylesheet" href="https://fonts.googleapis.com/css2?family=Alegreya:wght@400;500&display=swap">
<style>
  :root {
    --page: #ffffff;
    --card-yellow: #e8e891;
    --card-peach: #e6c8a0;
    --card-lilac: #a9a6ba;
    --ink: #151515;
    --brand-blue: #1a7cc6;
    --tagline-coral: #ec9478;
    --glow-green: rgba(140, 195, 90, 0.55);
    --glow-pink: rgba(240, 190, 220, 0.55);
  }
  html, body {
    margin: 0;
    padding: 0;
    width: 1200px;
    height: 703px;
    overflow: hidden;
    background: var(--page);
  }
  .canvas {
    position: relative;
    width: 1200px;
    height: 703px;
    background:
      radial-gradient(ellipse 150px 30px at 580px 0, var(--glow-pink), transparent 100%),
      var(--page);
  }
  .card {
    position: absolute;
    left: 23px;
    top: 23px;
    width: 1153px;
    height: 655px;
    background:
      radial-gradient(ellipse 380px 95px at 577px 520px, var(--glow-green) 0%, rgba(140, 195, 90, 0.25) 55%, rgba(140, 195, 90, 0) 100%),
      radial-gradient(ellipse 200px 185px at 567px 238px, var(--card-lilac) 0%, var(--card-lilac) 25%, rgba(230, 200, 160, 0) 100%),
      radial-gradient(ellipse 420px 290px at 567px 238px, var(--card-peach) 45%, rgba(230, 200, 160, 0) 100%),
      var(--card-yellow);
  }
  .card-text {
    position: absolute;
    left: 0;
    top: 0;
    width: 1153px;
    height: 655px;
  }
  .card-text text {
    font-family: "Alegreya", serif;
    fill: var(--ink);
  }
  .card-text .heading { font-size: 26px; }
  .card-text .person { font-size: 36px; }
  .card-text .detail { font-size: 23px; }
  .card-text .brand-name {
    font-size: 118px;
    font-weight: 500;
    fill: var(--brand-blue);
  }
  .card-text .tagline {
    font-size: 26px;
    fill: var(--tagline-coral);
  }
</style>
</head>
<body>
  <div class="canvas">
    <div class="card">
      <svg class="card-text" viewBox="0 0 1153 655" role="group" aria-label="Bright Fox booking contact details">
        <defs>
          <path id="arc-heading" d="M 300 183 Q 577 121 854 183"/>
          <path id="arc-person" d="M 400 250 Q 577 232 754 250"/>
          <path id="arc-email" d="M 320 327 Q 577 307 834 327"/>
        </defs>
        <text class="heading" text-anchor="middle">
          <textPath href="#arc-heading" startOffset="50%" textLength="528" lengthAdjust="spacing">For Bookings/Enquiries please contact:</textPath>
        </text>
        <text class="person" text-anchor="middle">
          <textPath href="#arc-person" startOffset="50%">Tilda Harwood</textPath>
        </text>
        <text class="detail" x="577" y="278" text-anchor="middle">T: 0498 217 503</text>
        <text class="detail" text-anchor="middle">
          <textPath href="#arc-email" startOffset="50%">enquiries@brightfoxparties.example.au</textPath>
        </text>
        <text class="detail" x="577" y="352" text-anchor="middle">ABN: 47 302 658 114</text>
        <text class="brand-name" x="577" y="529" text-anchor="middle" textLength="740" lengthAdjust="spacing">Bright Fox</text>
        <text class="tagline" x="577" y="589" text-anchor="middle" textLength="376" lengthAdjust="spacing">Kids Parties &amp; Events</text>
      </svg>
    </div>
  </div>
</body>
</html>
```